We own a sheep, cattle ect all type of fencing importing business. Based in the high country of New Zealand and are after a business card and logo to start with. We are after a look that is world class that is eye catching and professional.
Updates

Hi contact informo is Kowhai Ridge Fencing Solutions Malcolm and Heather Pryde P.O Box 52 Oxbury 7612 New Zealand Phone Number. +64 21938467 Email: hethpryde@tuimail.test malcolmpryde@tuimail.test Web: www.kowhairidgefencing.test Am open to any colours

Industry/Entity Type

Business

```html
<!DOCTYPE html>
<html lang="en">
<head>
<meta charset="utf-8">
<title>Kowhai Ridge Fencing Solutions – Business Card</title>
<link rel="stylesheet" href="https://fonts.googleapis.com/css2?family=PT+Sans&family=Hind:wght@400&display=swap">
<style>
  :root {
    --page-bg: #ffffff;
    --card-purple: #5b3f88;
    --card-purple-light: #6a4a96;
    --card-purple-deep: #40356f;
    --card-text: #ffffff;
    --title-shadow: rgba(30, 18, 60, 0.55);
  }
  * { margin: 0; padding: 0; box-sizing: border-box; }
  html, body {
    width: 1200px;
    height: 1000px;
    overflow: hidden;
    background: var(--page-bg);
  }
  .business-card {
    position: absolute;
    left: 168px;
    top: 220px;
    width: 882px;
    height: 530px;
    overflow: hidden;
    color: var(--card-text);
  }
  .card-backdrop {
    position: absolute;
    inset: 0;
    background:
      radial-gradient(ellipse at 45% 35%, var(--card-purple-light) 0%, transparent 60%),
      linear-gradient(160deg, var(--card-purple) 0%, var(--card-purple) 45%, var(--card-purple-deep) 100%);
  }
  .contact-block {
    position: absolute;
    left: 118px;
    top: 185px;
    font-family: "PT Sans", Tahoma, sans-serif;
  }
  .owner-names {
    font-size: 26px;
    font-weight: 400;
    line-height: 32px;
    margin-bottom: 8px;
  }
  .postal-address {
    font-size: 20px;
    line-height: 24px;
    font-style: normal;
    margin-bottom: 6px;
  }
  .phone-number {
    font-size: 21px;
    line-height: 28px;
    margin-bottom: 4px;
  }
  .email-list {
    list-style: none;
    font-size: 20px;
    line-height: 23px;
    margin-bottom: 5px;
  }
  .website {
    font-size: 20px;
    line-height: 26px;
  }
  .company-name {
    position: absolute;
    left: 474px;
    top: 192px;
    width: 400px;
    font-family: "Hind", "Segoe UI", sans-serif;
    font-weight: 400;
    font-size: 62px;
    line-height: 65px;
    text-shadow: 2px 3px 6px var(--title-shadow);
  }
</style>
</head>
<body>
  <section class="business-card">
    <div class="card-backdrop" role="img" aria-label="Purple background with a faint pattern of scattered rounded diamond shapes"></div>

    <div class="contact-block">
      <h2 class="owner-names">Malcolm and Heather Pryde</h2>
      <address class="postal-address">
        P.O Box 52<br>
        Oxbury 7612<br>
        New Zealand
      </address>
      <p class="phone-number">+64 21938467</p>
      <ul class="email-list">
        <li>hethpryde@tuimail.test</li>
        <li>malcolmpryde@tuimail.test</li>
      </ul>
      <p class="website">www.kowhairidgefencing.test</p>
    </div>

    <h1 class="company-name">Kowhai Ridge Fencing Solutions</h1>
  </section>
</body>
</html>
```